Stationery Design Project

We need a stationery design for a consultancy called 'Marrow Ridge'. The design should communicate innovation and professionalism. The colors used should complement our logo. Please include source files for winning design.

Requirements
Must have
• Logo with company name should be included. Font of the text in logo should not be altered. Paper should be A4 sized and not Letter sized.

```html
<!DOCTYPE html>
<html lang="en">
<head>
<meta charset="utf-8">
<title>Marrow Ridge — Business Card</title>
<link rel="stylesheet" href="https://fonts.googleapis.com/css2?family=Didact+Gothic&display=swap">
<style>
  :root {
    --backdrop: #3b3b3c;
    --paper: #ffffff;
    --paper-shade: #ededed;
    --charcoal-top: #2e2e2f;
    --charcoal-bottom: #1b1b1c;
    --edge-dark: #1f1f1f;
    --accent: #e08a1e;
    --ink: #2b2b2b;
    --ink-light: #d4d4d4;
  }
  * { margin: 0; padding: 0; box-sizing: border-box; }
  html, body {
    width: 1200px;
    height: 723px;
    overflow: hidden;
    background: var(--backdrop);
    font-family: "Didact Gothic", "Century Gothic", sans-serif;
  }
  .stage {
    width: 1200px;
    height: 723px;
    display: flex;
    justify-content: center;
    align-items: center;
    gap: 60px;
  }
  .card {
    position: relative;
    width: 300px;
    height: 520px;
    overflow: hidden;
  }

  /* Front */
  .card--front {
    background: linear-gradient(180deg, var(--paper) 0%, var(--paper-shade) 100%);
  }
  .brand {
    position: absolute;
    top: 56px;
    left: 0;
    right: 0;
    display: flex;
    flex-direction: column;
    align-items: center;
    gap: 18px;
  }
  .brand__mark {
    width: 86px;
    height: 86px;
    border-radius: 50%;
    background: var(--accent);
  }
  .brand__name {
    font-size: 27px;
    letter-spacing: 1px;
    color: var(--ink);
  }
  .front__details {
    position: absolute;
    left: 0;
    right: 0;
    bottom: 62px;
    text-align: center;
    font-size: 14px;
    line-height: 22px;
    color: var(--ink);
  }
  .front__stripe {
    position: absolute;
    left: 0;
    right: 0;
    bottom: 22px;
    height: 8px;
    background: var(--accent);
  }
  .front__base {
    position: absolute;
    left: 0;
    right: 0;
    bottom: 0;
    height: 22px;
    background: var(--edge-dark);
  }

  /* Back */
  .card--back {
    background: linear-gradient(180deg, var(--charcoal-top) 0%, var(--charcoal-bottom) 100%);
  }
  .person {
    position: absolute;
    top: 40px;
    left: 0;
    right: 0;
    text-align: center;
  }
  .person__name {
    font-size: 24px;
    color: var(--ink-light);
    letter-spacing: 0.5px;
  }
  .person__role {
    margin-top: 4px;
    font-size: 14px;
    color: var(--accent);
  }
  .contact {
    position: absolute;
    left: 56px;
    bottom: 56px;
    list-style: none;
    font-size: 15px;
    line-height: 24px;
    color: var(--ink-light);
  }
  .contact__label {
    color: var(--accent);
    margin-right: 4px;
  }
</style>
</head>
<body>
<main class="stage">
  <section class="card card--front">
    <div class="brand">
      <div class="brand__mark"></div>
      <div class="brand__name">Marrow Ridge</div>
    </div>
    <p class="front__details">42 Alder Lane, London N4 2QT<br>www.mridge.co.uk</p>
    <div class="front__stripe"></div>
    <div class="front__base"></div>
  </section>

  <section class="card card--back">
    <div class="person">
      <div class="person__name">Helena MARSH</div>
      <div class="person__role">Managing Partner</div>
    </div>
    <ul class="contact">
      <li><span class="contact__label">T:</span>+44 800 555 0132</li>
      <li><span class="contact__label">F:</span>+44 800 555 0147</li>
      <li><span class="contact__label">E:</span>info@mridge.co.uk</li>
    </ul>
  </section>
</main>
</body>
</html>
```